Certified Public Accountant specializing in tax preparation.

I need a business card designed that conveys knowledgeability, trustworthiness and competency. I am a licensed CPA and hold a Master's in taxation. As this is a personal service business, I would like to include my picture on the card.

```html
<!DOCTYPE html>
<html lang="en">
<head>
<meta charset="utf-8">
<title>Nora Vellant – Business Card</title>
<link rel="stylesheet" href="https://fonts.googleapis.com/css2?family=Open+Sans:wght@400&family=Roboto:ital,wght@0,400;0,500;0,700;1,400&display=swap">
<style>
  :root {
    --page-bg: #e8e5e2;
    --ink-black: #000000;
    --ink-dark: #111111;
    --paper: #ffffff;
    --paper-shade: #ececec;
    --band-grey: #8b8b8b;
    --text-light: #ffffff;
    --icon-pink: #f3d3e2;
    --portrait-top: #f2efef;
    --portrait-bottom: #ead3de;
  }
  * { margin: 0; padding: 0; box-sizing: border-box; }
  html, body {
    width: 1200px;
    height: 900px;
    overflow: hidden;
    background: var(--page-bg);
  }
  .card {
    position: absolute;
    left: 150px;
    top: 171px;
    width: 900px;
    height: 558px;
    background: var(--paper);
    overflow: hidden;
    box-shadow: 0 10px 30px rgba(0,0,0,0.18);
  }
  .contact-band {
    position: absolute;
    left: 0; top: 0;
    width: 682px; height: 257px;
    background: var(--ink-black);
  }
  .contact-list {
    position: absolute;
    left: 44px; top: 82px;
    list-style: none;
    font-family: "Open Sans", Arial, sans-serif;
    font-size: 25px;
    line-height: 32px;
    color: var(--text-light);
  }
  .contact-list li { display: flex; align-items: center; gap: 8px; }
  .contact-icon { width: 22px; height: 22px; fill: var(--icon-pink); }
  .name-band {
    position: absolute;
    left: 0; top: 257px;
    width: 500px; height: 168px;
    background: linear-gradient(90deg, var(--paper) 0%, var(--paper-shade) 100%);
  }
  .person-name {
    position: absolute;
    left: 46px; top: 34px;
    font-family: "Roboto", Arial, sans-serif;
    font-weight: 700;
    font-size: 33px;
    letter-spacing: 0.5px;
    color: var(--ink-dark);
  }
  .credentials {
    position: absolute;
    left: 46px; top: 80px;
    font-family: "Roboto", Arial, sans-serif;
    font-style: italic;
    font-size: 23px;
    line-height: 32px;
    color: var(--ink-dark);
  }
  .role-band {
    position: absolute;
    left: 0; top: 425px;
    width: 500px; height: 133px;
    background: var(--band-grey);
    color: var(--text-light);
    font-family: "Roboto", Arial, sans-serif;
  }
  .role-title {
    position: absolute;
    left: 48px; top: 20px;
    font-size: 24px;
  }
  .company-name {
    position: absolute;
    left: 48px; top: 62px;
    font-size: 30px;
    font-weight: 700;
  }
  .portrait {
    position: absolute;
    left: 500px; top: 0;
    width: 400px; height: 558px;
    background: linear-gradient(180deg, var(--portrait-top) 0%, var(--portrait-bottom) 100%);
  }
</style>
</head>
<body>
  <div class="card">
    <div class="contact-band">
      <ul class="contact-list">
        <li>
          <svg class="contact-icon" viewBox="0 0 24 24" aria-hidden="true"><path d="M3 8c0-2 4-4 9-4s9 2 9 4v2h-5V8H8v2H3z M6 11h12l2 8H4z M10 13h4v4h-4z"/></svg>
          <span>555-204-7731</span>
        </li>
        <li>
          <svg class="contact-icon" viewBox="0 0 24 24" aria-hidden="true"><path d="M6 3h12v5H6z M3 9h18v8h-3v-3H6v3H3z M7 15h10v6H7z"/></svg>
          <span>555-204-7790</span>
        </li>
        <li>
          <svg class="contact-icon" viewBox="0 0 24 24" aria-hidden="true"><path d="M3 6h18v12H3z"/><path d="M3 6l9 7 9-7" fill="none" stroke="#000" stroke-width="1.6"/></svg>
          <span>nora@clearledgertax.com</span>
        </li>
      </ul>
    </div>

    <div class="name-band">
      <h1 class="person-name">NORA VELLANT</h1>
      <p class="credentials">Licensed Certified Public Accountant<br>MAcc</p>
    </div>

    <div class="role-band">
      <p class="role-title">President</p>
      <p class="company-name">Clear Ledger Tax</p>
    </div>

    <div class="portrait" role="img" aria-label="Portrait photo of the accountant in a pink blazer against a light background"></div>
  </div>
</body>
</html>
```